Granite Tile Retail Website

We need wireframe PSD for a website selling granite tile. There are 4 custom pages, shopping cart page, and checkout page. I have a logo designed but the color scheme is up to you.
Color Gallery - We have approximately 20 different stone colors. Each color will have a little gallery of its own pictures. On this page the customer can also add a sample piece of the color they are viewing to their shopping cart.
Questions Page - This page has 3 elements
1. Upload or fax diagram of kitchen for quotation
2. Installation video
3. Installation FAQ (text)
Order Page - This page has 3 steps for the customer
1. Customer chooses his color.
2. For each color we have numerous different products. He inputs the quantity of each product.
3. Customer is given total price and shipping quote. If order over $500 it says "This order qualifies for free shipping". Customer can click on button to "Order Now"
Shopping Cart - Very standard, just like I have attached here. Just modify for your colors / font.
Checkout - Just like in the attached. See design-explanation.docx for minor adjustments.
I have vector file for logo.
Please try to post your designs by tonightÂ
Home owners 40-60 years old
Shopping

```html
<!DOCTYPE html>
<html lang="en">
<head>
<meta charset="utf-8">
<title>Stonewell Granite – Order Colors</title>
<link rel="stylesheet" href="https://fonts.googleapis.com/css2?family=Oswald:wght@400;500&family=Open+Sans:wght@400;600&display=swap">
<style>
:root{
  --page-bg:#f6f6f6;
  --panel:#ffffff;
  --line:#e2e2e2;
  --ink:#333333;
  --ink-soft:#4a4a4a;
  --brand:#5a1a2a;
  --accent:#e3a95a;
  --gold-top:#efbb5a;
  --gold-bot:#d6962c;
  --gold-edge:#c4862a;
  --banner-top:#4a4640;
  --banner-bot:#1f1d1a;
  --banner-text:#f0b84e;
  --red:#d3103c;
  --table-line:#b9b9b9;
  --table-head:#efefef;
}
*{box-sizing:border-box;margin:0;padding:0}
html,body{width:1098px;height:1200px;overflow:hidden}
body{background:var(--page-bg);font-family:"Open Sans",Arial,sans-serif;color:var(--ink);position:relative}
.abs{position:absolute}
.page{left:40px;top:40px;width:1000px;height:1091px;background:var(--panel);border:1px solid var(--line)}
.header{left:60px;top:65px;width:960px;height:121px;border-top:1px solid var(--line);border-bottom:1px solid var(--line);background:linear-gradient(#ffffff,#efefef)}
.brand{left:90px;top:92px;display:flex;align-items:center;gap:12px;font-family:"Oswald",sans-serif;font-weight:500;color:var(--brand);line-height:1}
.brand-mark{width:30px;height:30px;background:var(--brand)}
.brand-name{font-size:38px;letter-spacing:1px}
.brand-sub{font-size:18px;letter-spacing:6px;margin-top:4px}
.nav{right:58px;top:96px;height:58px;display:flex;align-items:center;font-family:"Oswald",sans-serif;font-size:21px;color:#3b3b3b}
.nav a{color:inherit;text-decoration:none;padding:0 11px;line-height:58px;border-left:1px solid #9a9a9a}
.nav a:first-child{border-left:none}
.nav a.current{color:var(--accent)}
.page-title{left:71px;top:218px;font-family:"Oswald",sans-serif;font-size:25px;color:#3a3a3a}
.step{left:60px;width:253px;height:60px}
.step span{position:absolute;left:28px;top:6px;font-family:"Oswald",sans-serif;font-size:25px;color:var(--banner-text)}
.select{left:81px;top:340px;width:245px;height:31px;border:1px solid #bcbcbc;font-size:16px;padding:4px 11px;color:#333}
.select i{position:absolute;right:3px;top:3px;width:25px;height:23px;border:1px solid #aaa;background:linear-gradient(#fff,#e6e6e6)}
.hint{font-size:13px;color:#444}
.swatch-label{font-family:"Oswald",sans-serif;font-size:11px;color:#333}
.swatch{width:107px;height:68px;border:3px solid}
.arrow{width:20px;height:20px}
.qty-box{width:45px;height:26px;border:1px solid #c4c4c4}
.qty-label{font-size:16px;color:#333}
.btn{background:linear-gradient(var(--gold-top),var(--gold-bot));border:2px solid var(--gold-edge);font-family:"Oswald",sans-serif;color:#2a2418;display:flex;align-items:center;justify-content:center}
.price{left:310px;top:800px;width:652px;height:84px;border-collapse:collapse;font-size:17px;letter-spacing:1px}
.price th,.price td{border:2px solid var(--table-line);text-align:center;font-weight:400}
.price th{background:var(--table-head);height:30px;color:#444}
.price td{height:52px}
.price .total{color:var(--red);font-weight:600;font-size:21px}
.footer{left:60px;top:1005px;width:960px;height:115px;border-top:1px solid var(--line);background:linear-gradient(#ffffff,#f0f0f0)}
.foot-col{top:1023px;font-family:"Oswald",sans-serif;font-size:13.5px;line-height:19.2px;color:#2e1a1e;list-style:none}
.foot-col .current{color:var(--accent)}
</style>
</head>
<body>
<div class="abs page"></div>

<header class="abs header"></header>
<div class="abs brand">
  <div class="brand-mark"></div>
  <div><div class="brand-name">STONEWELL</div><div class="brand-sub">GRANITE</div></div>
</div>
<nav class="abs nav">
  <a>HOME</a><a>GALLERY</a><a>QUESTIONS</a><a class="current">ORDER</a><a>SHOPPING CART</a>
</nav>

<h1 class="abs page-title">ORDER COLORS</h1>

<svg width="0" height="0" style="position:absolute">
  <defs>
    <linearGradient id="bannerFill" x1="0" y1="0" x2="0" y2="1">
      <stop offset="0" stop-color="#4a4640"/><stop offset="1" stop-color="#1f1d1a"/>
    </linearGradient>
  </defs>
</svg>

<div class="abs step" style="top:261px">
  <svg width="253" height="60"><polygon points="0,0 253,0 253,44 126,60 0,44" fill="url(#bannerFill)"/><polygon points="0,44 126,60 253,44 253,46 126,62 0,46" fill="#888"/></svg>
  <span>01.&nbsp;&nbsp;&nbsp; PICK COLOR</span>
</div>
<div class="abs select">Name of a Granite Color<i><svg width="23" height="21"><path d="M8 6l3.5 4 3.5-4M8 11l3.5 4 3.5-4" stroke="#333" stroke-width="1.6" fill="none"/></svg></i></div>
<p class="abs hint" style="left:93px;top:379px">See your options on the right</p>

<!-- color swatches -->
<span class="abs swatch-label" style="left:401px;top:300px">01. GIALLO</span>
<span class="abs swatch-label" style="left:523px;top:300px">02. TAR BROWN</span>
<span class="abs swatch-label" style="left:645px;top:300px">05. GIALLO</span>
<span class="abs swatch-label" style="left:768px;top:300px">06. TAR BROWN</span>
<span class="abs swatch-label" style="left:890px;top:300px">09. GIALLO</span>
<div class="abs swatch" style="left:401px;top:314px;background:#a77a58;border-color:#8b5f40"></div>
<div class="abs swatch" style="left:523px;top:314px;background:#d8b9a0;border-color:#c5a386"></div>
<div class="abs swatch" style="left:645px;top:314px;background:#3c3d2e;border-color:#222"></div>
<div class="abs swatch" style="left:768px;top:314px;background:#4d1828;border-color:#2a0d15"></div>
<div class="abs swatch" style="left:890px;top:314px;background:#7c6a5a;border-color:#5e4e40"></div>

<span class="abs swatch-label" style="left:401px;top:384px">03. MERT BROWN</span>
<span class="abs swatch-label" style="left:523px;top:384px">04. VBA TUBA</span>
<span class="abs swatch-label" style="left:645px;top:384px">07. MERT BROWN</span>
<span class="abs swatch-label" style="left:768px;top:384px">08. VBA TUBA</span>
<span class="abs swatch-label" style="left:890px;top:384px">11. MERT BROWN</span>
<div class="abs swatch" style="left:401px;top:398px;background:#f1e0d0;border-color:#d9c0a8"></div>
<div class="abs swatch" style="left:523px;top:398px;background:#5a2c18;border-color:#3a1a0c"></div>
<div class="abs swatch" style="left:645px;top:398px;background:#2d2f33;border-color:#111"></div>
<div class="abs swatch" style="left:768px;top:398px;background:#858a95;border-color:#5e6470"></div>
<div class="abs swatch" style="left:890px;top:398px;background:#a68078;border-color:#7c5a52"></div>

<svg class="abs arrow" style="left:373px;top:381px" viewBox="0 0 20 20"><circle cx="10" cy="10" r="9.5" fill="#9c9c9c"/><path d="M12.5 5l-5 5 5 5M8 10h7" stroke="#fff" stroke-width="2.2" fill="none"/></svg>
<svg class="abs arrow" style="left:1001px;top:381px" viewBox="0 0 20 20"><circle cx="10" cy="10" r="9.5" fill="#1e1e1e"/><path d="M7.5 5l5 5-5 5M12 10H5" stroke="#fff" stroke-width="2.2" fill="none"/></svg>

<div class="abs step" style="top:500px">
  <svg width="253" height="60"><polygon points="0,0 253,0 253,44 126,60 0,44" fill="url(#bannerFill)"/><polygon points="0,44 126,60 253,44 253,46 126,62 0,46" fill="#888"/></svg>
  <span>02.&nbsp; INPUT QUANTITIES</span>
</div>
<p class="abs hint" style="left:93px;top:573px">Visit our <span style="border-bottom:1px solid #444">Questions Page</span> if you need help calculating</p>

<div class="abs qty-box" style="left:81px;top:609px"></div><span class="abs qty-label" style="left:138px;top:612px">12x12</span>
<div class="abs qty-box" style="left:81px;top:644px"></div><span class="abs qty-label" style="left:138px;top:647px">18x21</span>
<div class="abs qty-box" style="left:241px;top:609px"></div><span class="abs qty-label" style="left:297px;top:612px">Bullnose</span>
<div class="abs qty-box" style="left:241px;top:644px"></div><span class="abs qty-label" style="left:297px;top:647px">EZ Tile</span>
<div class="abs qty-box" style="left:401px;top:609px"></div><span class="abs qty-label" style="left:457px;top:612px">24" Ogee</span>
<div class="abs qty-box" style="left:401px;top:644px"></div><span class="abs qty-label" style="left:457px;top:647px">24" Bullnose</span>
<div class="abs qty-box" style="left:575px;top:609px"></div><span class="abs qty-label" style="left:631px;top:612px">Right Corner</span>
<div class="abs qty-box" style="left:575px;top:644px"></div><span class="abs qty-label" style="left:631px;top:647px">Left Corner</span>
<div class="abs qty-box" style="left:765px;top:609px"></div><span class="abs qty-label" style="left:821px;top:612px">Inside corner</span>
<div class="abs qty-box" style="left:765px;top:644px"></div><span class="abs qty-label" style="left:821px;top:647px">Sink Kit</span>

<div class="abs step" style="top:720px">
  <svg width="253" height="60"><polygon points="0,0 253,0 253,44 126,60 0,44" fill="url(#bannerFill)"/><polygon points="0,44 126,60 253,44 253,46 126,62 0,46" fill="#888"/></svg>
  <span>03.&nbsp;&nbsp;&nbsp; GET PRICE</span>
</div>
<div class="abs btn" style="left:81px;top:799px;width:208px;height:58px;font-size:27px">CALCULATE NOW</div>

<table class="abs price">
  <tr><th>Stone:</th><th>Shipping:</th><th>Tax:</th><th class="total" style="width:262px">Gand total:</th></tr>
  <tr><td>$ 550</td><td>$0</td><td>$ 0</td><td class="total">$ 550</td></tr>
</table>

<div class="abs btn" style="left:678px;top:910px;width:318px;height:76px;font-size:36px;gap:18px">
  <svg width="44" height="40" viewBox="0 0 44 40"><path d="M2 4h7l5 22h22l5-16H12" stroke="#1e1e1e" stroke-width="3.5" fill="none" stroke-linejoin="round"/><rect x="13" y="12" width="25" height="12" fill="#1e1e1e"/><circle cx="16" cy="34" r="3.5" fill="#1e1e1e"/><circle cx="34" cy="34" r="3.5" fill="#1e1e1e"/></svg>
  ADD TO CART
</div>

<footer class="abs footer"></footer>
<ul class="abs foot-col" style="left:91px"><li>HOME</li><li>GALLERY</li><li>QUESTIONS</li><li class="current">ORDER</li><li>SHOPPING CART</li></ul>
<ul class="abs foot-col" style="left:304px"><li>RETURN POLICY</li><li>SHIPPING POLICY</li><li>PRIVACY</li><li>TERMS OF USE</li><li>CUSTOMER SERVICE</li></ul>
<ul class="abs foot-col" style="left:540px"><li>NEW LINK</li><li>ANOTHER LINK</li><li>THIRD LINK</li><li>FOURTH LINK</li><li>FIFTH LINK</li></ul>

<div class="abs" role="img" aria-label="Payment processor verification seal" style="left:796px;top:1026px;width:62px;height:58px;border-radius:50%;background:radial-gradient(#f3e6a8,#c9b24a)"></div>
<div class="abs" role="img" aria-label="Accredited business badge" style="left:874px;top:1026px;width:116px;height:44px;border-radius:4px;background:#1d5c86"></div>
<div class="abs" role="img" aria-label="Secure payment badge" style="left:874px;top:1078px;width:116px;height:40px;border-radius:4px;background:linear-gradient(#e9eef5,#cfd9e6)"></div>
</body>
</html>
```